Tallgrove Vale Management

I need a professional website. My current website is tallgrovevalemanagement.com and I hate it. It was created with some AI tool very quickly because I needed a site up and running with no advanced notice. I’m open to all designs .. I trust you, the professionals will deliver the results I’m anxiously awaiting! :)

```html
<!DOCTYPE html>
<html lang="en">
<head>
<meta charset="utf-8">
<title>Tallgrove Vale Management</title>
<link href="https://fonts.googleapis.com/css2?family=Poppins:wght@400;500;600;700&display=swap" rel="stylesheet">
<style>
:root{
  --red:#a71c25;
  --red-bright:#c8262d;
  --navy:#22335a;
  --ink:#222;
  --muted:#444;
  --rule:#888;
  --light:#f0f0f0;
  --white:#fff;
}
*{margin:0;padding:0;box-sizing:border-box}
html,body{width:1200px;height:4170px;overflow:hidden}
body{font-family:'Poppins',sans-serif;color:var(--ink);background:var(--white);position:relative}
.abs{position:absolute}
.btn{position:absolute;display:flex;align-items:center;justify-content:center;font-weight:600;text-transform:uppercase;color:var(--white);text-decoration:none}
.btn-pill{border-radius:999px}

/* header */
.site-header{position:absolute;left:0;top:0;width:1200px;height:113px;background:var(--white)}
.brand{position:absolute;left:54px;top:30px;display:flex;align-items:center;gap:10px}
.brand-dot{width:22px;height:22px;border-radius:50%;background:var(--red)}
.brand-name{font-weight:700;font-size:17px;color:var(--navy);line-height:1.15;width:150px}
.nav{position:absolute;top:48px;font-size:13px;font-weight:500;color:var(--ink)}
.nav.active{color:var(--red)}
.header-cta{left:962px;top:32px;width:171px;height:52px;background:var(--red);font-size:15px}

/* hero */
.hero{position:absolute;left:0;top:113px;width:1200px;height:622px;background:var(--light)}
.hero-photo{position:absolute;left:0;top:0;width:1200px;height:622px;
  background:linear-gradient(90deg,var(--light) 0%,var(--light) 36%,rgba(240,240,240,0) 60%),
  linear-gradient(180deg,#b9cde0 0%,#cdd9e2 18%,#7e9a62 32%,#5f7f45 55%,#6f8b55 75%,#4f6d3a 100%)}
.hero-title{left:71px;top:283px;font-size:46px;font-weight:700;line-height:1.25;color:var(--navy)}
.hero-text{left:71px;top:405px;width:540px;font-size:14px;line-height:26px;color:var(--ink)}
.hero-cta{left:71px;top:474px;width:165px;height:49px;background:var(--red);font-size:15px}

/* section titles */
.section-title{font-size:40px;font-weight:700;text-transform:uppercase;color:var(--navy);line-height:1}
.section-title .accent{color:var(--red-bright)}
.title-rule{height:3px;background:var(--rule)}

/* services */
.services-title{left:0;width:1200px;top:880px;text-align:center}
.services-rule{left:567px;top:931px;width:66px}
.card{position:absolute;top:984px;width:345px;height:467px;background:var(--white);box-shadow:0 2px 10px rgba(0,0,0,.14)}
.card-media{position:absolute;left:18px;top:18px;width:310px;height:228px}
.card-title{position:absolute;left:0;width:100%;top:274px;text-align:center;font-size:17px;font-weight:600;color:var(--red);text-transform:uppercase}
.card-text{position:absolute;left:30px;width:285px;top:306px;text-align:center;font-size:13.5px;line-height:25px;color:var(--muted)}
.card-btn{left:111px;top:395px;width:123px;height:48px;background:var(--navy);font-size:11.5px;border-radius:3px}
.services-all{left:360px;top:1515px;width:199px;height:56px;background:var(--red);font-size:14px}
.services-request{left:578px;top:1515px;width:256px;height:56px;border:2px solid var(--red);color:var(--red);font-size:13.5px;font-weight:500}

/* about */
.about-media{left:66px;top:1789px;width:457px;height:408px;background:linear-gradient(160deg,#d8d2c7 0%,#c2b9ab 45%,#ddd3c1 70%,#b9ad98 100%)}
.about-title{left:628px;top:1771px}
.about-rule{left:628px;top:1822px;width:110px}
.about-sub{left:628px;top:1838px;font-size:21px;font-weight:500;color:var(--ink)}
.about-text{left:628px;width:475px;font-size:14px;line-height:25.4px;color:var(--muted);text-align:justify}
.about-cta{left:628px;top:2166px;width:125px;height:42px;background:var(--navy);font-size:13px}

/* banner */
.banner{position:absolute;left:0;top:2386px;width:1200px;height:483px;background:var(--navy);overflow:hidden}
.banner-title{position:absolute;left:440px;width:730px;top:100px;text-align:center;font-size:60px;font-weight:700;line-height:1.05;color:var(--white);text-transform:uppercase}
.banner-text{position:absolute;left:440px;width:730px;top:249px;text-align:center;font-size:18px;line-height:26px;color:var(--white)}
.banner-cta{left:709px;top:329px;width:193px;height:52px;background:var(--red);font-size:16px}

/* contact */
.contact-title{left:66px;top:3026px}
.contact-rule{left:66px;top:3077px;width:68px}
.contact-intro{left:66px;top:3106px;font-size:13.5px;color:var(--ink)}
.field{position:absolute;background:var(--white);box-shadow:0 1px 6px rgba(0,0,0,.16);font-size:15px;color:#b5b5b5;padding:0 12px;display:flex;align-items:center}
.field-message{align-items:flex-start;padding-top:38px}
.contact-submit{left:66px;top:3447px;width:176px;height:42px;background:var(--navy);font-size:12.5px}
.contact-media{left:680px;top:3053px;width:452px;height:368px;background:radial-gradient(ellipse at 55% 50%,#e6d8c6 0%,#c9b59c 45%,#8d7d6a 100%)}

/* footer */
.footer{position:absolute;left:0;top:3688px;width:1200px;height:482px;background:var(--navy);color:var(--white)}
.footer-brand{position:absolute;left:96px;top:170px;width:220px;display:flex;align-items:center;justify-content:center;gap:10px}
.footer-brand .brand-name{color:var(--white);font-size:18px;width:160px}
.social{position:absolute;top:306px;width:38px;height:38px;border-radius:50%;background:var(--white);display:flex;align-items:center;justify-content:center}
.social::after{content:"";width:12px;height:12px;border-radius:50%;background:var(--red-bright)}
.footer-heading{position:absolute;top:126px;font-size:23px;font-weight:500}
.footer-rule{position:absolute;top:167px;width:66px;height:2px;background:#9aa3b8}
.footer-link{position:absolute;left:492px;font-size:14px}
.footer-link::before{content:"";position:absolute;left:-20px;top:6px;width:7px;height:7px;border-radius:50%;background:var(--red-bright)}
.footer-icon{position:absolute;left:742px;width:38px;height:38px;border-radius:50%;background:var(--white)}
.footer-icon svg{position:absolute;left:10px;top:10px}
.footer-info{position:absolute;left:792px;font-size:14px;line-height:24px}
.footer-divider{position:absolute;left:66px;top:390px;width:1068px;height:1px;background:#5c6a8a}
.copyright{position:absolute;left:0;width:1200px;top:425px;text-align:center;font-size:14.5px}
</style>
</head>
<body>

<header class="site-header">
  <div class="brand"><span class="brand-dot"></span><span class="brand-name">Tallgrove Vale Management</span></div>
  <span class="nav active" style="left:704px">HOME</span>
  <span class="nav" style="left:774px">ABOUT US</span>
  <span class="nav" style="left:866px">SERVICES</span>
  <a class="btn btn-pill header-cta">Contact Us</a>
</header>

<section class="hero">
  <div class="hero-photo" role="img" aria-label="Aerial view of a leafy residential neighbourhood with a city skyline in the distance"></div>
</section>
<h1 class="abs hero-title">A TRUE PARTNER,<br>NOT JUST A VENDOR.</h1>
<p class="abs hero-text">Drawing on decades of collective expertise, the team facilitates regulatory compliance, cost efficiency, and proactive maintenance.</p>
<a class="btn btn-pill hero-cta">Contact Now</a>

<h2 class="abs section-title services-title"><span class="accent">Our</span> Services</h2>
<div class="abs title-rule services-rule"></div>

<article class="card" style="left:66px">
  <div class="card-media" role="img" aria-label="Hands arranging material samples on a wooden table" style="background:linear-gradient(135deg,#c9a987,#e6d6bf 55%,#a88a6a)"></div>
  <h3 class="card-title">Basic Service</h3>
  <p class="card-text">Lorem ipsum dolor sit amet, consectetur adipiscing elit, sed do eiusmod tempor incididunt ut labore et dolore magna...</p>
  <a class="btn card-btn">Read More</a>
</article>
<article class="card" style="left:426px">
  <div class="card-media" role="img" aria-label="Modern bathroom vanity with a round mirror and black tap" style="background:linear-gradient(160deg,#a59888,#d8cabb 50%,#b9a995)"></div>
  <h3 class="card-title">Intermediate Service</h3>
  <p class="card-text">Lorem ipsum dolor sit amet, consectetur adipiscing elit, sed do eiusmod tempor incididunt ut labore et dolore magna...</p>
  <a class="btn card-btn">Read More</a>
</article>
<article class="card" style="left:785px">
  <div class="card-media" role="img" aria-label="Desk with a laptop, lamp and vase of lilies" style="background:linear-gradient(150deg,#8e7765,#d8cbbd 55%,#efe7dc)"></div>
  <h3 class="card-title">Advanced Service</h3>
  <p class="card-text">Lorem ipsum dolor sit amet, consectetur adipiscing elit, sed do eiusmod tempor incididunt ut labore et dolore magna...</p>
  <a class="btn card-btn">Read More</a>
</article>

<a class="btn services-all">View All Services</a>
<a class="btn services-request">Request Your Service Type</a>

<div class="abs about-media" role="img" aria-label="Stack of timber blocks topped with a stone slab"></div>
<h2 class="abs section-title about-title"><span class="accent">About</span> Us</h2>
<div class="abs title-rule about-rule"></div>
<h3 class="abs about-sub">About Our Property Management Solutions</h3>
<p class="abs about-text" style="top:1872px">Our organization delivers comprehensive property management solutions that optimize asset performance and tenant satisfaction. By integrating advanced analytics with proven operational frameworks, our specialists ensure each property achieves sustained value appreciation.</p>
<p class="abs about-text" style="top:2024px">Drawing on decades of collective expertise, the team facilitates regulatory compliance, cost efficiency, and proactive maintenance. This disciplined approach enables owners to preserve capital, enhance occupancy rates, and demonstrate long-term resilience across diverse market conditions.</p>
<a class="btn btn-pill about-cta">Read More</a>

<section class="banner">
  <svg class="abs" style="left:0;top:0" width="460" height="483" viewBox="0 0 460 483" role="img" aria-label="Sculpted white sphere with carved ridges on a pale surface">
    <defs>
      <linearGradient id="bannerPhoto" x1="0" y1="0" x2="1" y2="1">
        <stop offset="0" stop-color="#cfc9c0"/>
        <stop offset=".5" stop-color="#e3ddd3"/>
        <stop offset="1" stop-color="#a9a197"/>
      </linearGradient>
    </defs>
    <path d="M0 0 H230 C400 40 470 230 430 330 C400 410 360 460 330 483 H0 Z" fill="url(#bannerPhoto)"/>
  </svg>
  <h2 class="banner-title">Expertise Rooted in Asset Preservation</h2>
  <p class="banner-text">The organization applies rigorously tested frameworks and data-driven methodologies to safeguard property value while elevating tenant experience.</p>
  <a class="btn btn-pill banner-cta">Learn More</a>
</section>

<h2 class="abs section-title contact-title"><span class="accent">Contact</span> Us</h2>
<div class="abs title-rule contact-rule"></div>
<p class="abs contact-intro">For more information,Please fill out the following and we will be in touch shortly</p>
<div class="field" style="left:66px;top:3159px;width:261px;height:51px">First Name</div>
<div class="field" style="left:350px;top:3159px;width:262px;height:51px">Second Name</div>
<div class="field" style="left:66px;top:3238px;width:261px;height:52px">Phone</div>
<div class="field" style="left:350px;top:3238px;width:262px;height:52px">Subject</div>
<div class="field field-message" style="left:66px;top:3312px;width:546px;height:101px">Message</div>
<a class="btn btn-pill contact-submit">Submit a Message</a>
<div class="abs contact-media" role="img" aria-label="Architectural model of a modern house with warm interior lighting"></div>

<footer class="footer">
  <div class="footer-brand"><span class="brand-dot"></span><span class="brand-name">Tallgrove Vale Management</span></div>
  <span class="social" style="left:140px" aria-label="Social profile"></span>
  <span class="social" style="left:188px" aria-label="Social profile"></span>
  <span class="social" style="left:235px" aria-label="Social profile"></span>

  <h4 class="footer-heading" style="left:470px">LINKS</h4>
  <div class="footer-rule" style="left:470px"></div>
  <span class="footer-link" style="top:196px">About Us</span>
  <span class="footer-link" style="top:228px">Services</span>
  <span class="footer-link" style="top:260px">Contact</span>

  <h4 class="footer-heading" style="left:740px">CONTACT</h4>
  <div class="footer-rule" style="left:740px"></div>
  <span class="footer-icon" style="top:194px"><svg width="18" height="18" viewBox="0 0 24 24"><path d="M12 2a7 7 0 0 0-7 7c0 5 7 13 7 13s7-8 7-13a7 7 0 0 0-7-7zm0 9.5A2.5 2.5 0 1 1 12 6.5a2.5 2.5 0 0 1 0 5z" fill="#c8262d"/></svg></span>
  <p class="footer-info" style="top:189px">Lorem ipsum,Lorem ipsum,<br>Lorem ipsum</p>
  <span class="footer-icon" style="top:254px"><svg width="18" height="18" viewBox="0 0 24 24"><path d="M6.6 10.8a15 15 0 0 0 6.6 6.6l2.2-2.2a1 1 0 0 1 1-.25 11.4 11.4 0 0 0 3.6.57 1 1 0 0 1 1 1V20a1 1 0 0 1-1 1A17 17 0 0 1 3 4a1 1 0 0 1 1-1h3.5a1 1 0 0 1 1 1c0 1.25.2 2.45.57 3.57a1 1 0 0 1-.25 1z" fill="#c8262d"/></svg></span>
  <p class="footer-info" style="top:261px">(555) 014 2876</p>
  <span class="footer-icon" style="top:308px"><svg width="18" height="18" viewBox="0 0 24 24"><path d="M3 5h18v14H3z" fill="#c8262d"/><path d="M3 5l9 7 9-7" fill="none" stroke="#fff" stroke-width="1.6"/></svg></span>
  <p class="footer-info" style="top:315px">info@tallgrovevalemanagement.com</p>

  <div class="footer-divider"></div>
  <p class="copyright">Copyright © 2026 All Rights Reserved By Company Name</p>
</footer>

</body>
</html>
```